Business Cards & Stationary for Solo Attorney
Marcus Tolland Counsellor At Law
Business Cards & Stationary for Solo Attorney - Law
Creative Brief
Professional
Marcus Tolland
Counsellor At Law
482 Brindlecombe Avenue, 7th Floor Fernmoor, Ostvale 08347
mtollandlaw@quillpost.example
tollandlawfirm.example

```html
<!DOCTYPE html>
<html lang="en">
<head>
<meta charset="UTF-8">
<title>Marcus Tolland – Business Card</title>
<link href="https://fonts.googleapis.com/css2?family=Cinzel:wght@400;600&display=swap" rel="stylesheet">
<style>
  :root {
    --navy: #2d375f;
    --navy-text: #2f3a66;
    --paper: #ffffff;
    --backdrop: #e9e7e3;
    --tab-grey: #8d8f96;
    --ink-light: #ffffff;
  }
  * { box-sizing: border-box; margin: 0; padding: 0; }
  html, body {
    width: 1200px; height: 900px; overflow: hidden;
    background: var(--backdrop);
  }
  .canvas { position: relative; width: 1200px; height: 900px; }
  .business-card {
    position: absolute; left: 110px; top: 170px;
    width: 980px; height: 560px;
    background: var(--paper);
    box-shadow: 0 10px 30px rgba(0,0,0,0.18);
    overflow: hidden;
    font-family: "Cinzel", serif;
  }
  .brand {
    position: absolute; left: 230px; top: 78px;
    display: flex; align-items: center; gap: 22px;
  }
  .brand-mark {
    width: 96px; height: 96px; border-radius: 50%;
    background: var(--navy);
  }
  .brand-text { color: var(--navy-text); }
  .brand-name {
    font-weight: 600; font-size: 44px; line-height: 1.05; letter-spacing: 1px;
  }
  .brand-tagline {
    display: flex; align-items: center; gap: 10px;
    font-size: 22px; letter-spacing: 2px; margin-top: 4px;
  }
  .brand-tagline::before, .brand-tagline::after {
    content: ""; flex: 1; height: 2px; background: var(--navy-text);
  }
  .brand-tagline::before { flex: 0 0 18px; }
  .info-band {
    position: absolute; left: 0; top: 248px;
    width: 100%; height: 218px;
    background: var(--navy);
    color: var(--ink-light);
  }
  .band-tab {
    position: absolute; left: 0; top: 142px;
    width: 14px; height: 44px;
    background: var(--tab-grey);
  }
  .holder { position: absolute; left: 40px; top: 136px; }
  .holder-name { font-size: 22px; font-weight: 600; letter-spacing: 0.5px; }
  .holder-title { font-size: 17px; margin-top: 4px; }
  .contact-list {
    position: absolute; left: 560px; top: 28px;
    list-style: none; font-size: 15px; line-height: 1.3;
  }
  .contact-item {
    display: flex; align-items: flex-start; gap: 10px; margin-bottom: 3px;
  }
  .contact-icon { flex: none; width: 16px; height: 16px; margin-top: 2px; }
</style>
</head>
<body>
<main class="canvas">
  <section class="business-card">
    <header class="brand">
      <div class="brand-mark"></div>
      <div class="brand-text">
        <p class="brand-name">Marcus Tolland</p>
        <p class="brand-tagline">Counsellor At Law</p>
      </div>
    </header>

    <div class="info-band">
      <div class="band-tab"></div>
      <div class="holder">
        <p class="holder-name">Marcus Tolland</p>
        <p class="holder-title">Counsellor At Law</p>
      </div>

      <ul class="contact-list">
        <li class="contact-item">
          <svg class="contact-icon" viewBox="0 0 16 16"><circle cx="8" cy="8" r="8" fill="#fff"/><path d="M8 3.5a2.6 2.6 0 0 0-2.6 2.6C5.4 8 8 12 8 12s2.6-4 2.6-5.9A2.6 2.6 0 0 0 8 3.5z" fill="#2d375f"/><circle cx="8" cy="6.1" r="1" fill="#fff"/></svg>
          <span>482 Brindlecombe Avenue, 7th Floor<br>Fernmoor, Ostvale 08347</span>
        </li>
        <li class="contact-item">
          <svg class="contact-icon" viewBox="0 0 16 16"><circle cx="8" cy="8" r="8" fill="#fff"/><path d="M5.3 4.2l1.4-.3 .8 2-1 .8a5 5 0 0 0 2.4 2.4l.8-1 2 .8-.3 1.4c-3.6.4-6.5-2.5-6.1-6.1z" fill="#2d375f"/></svg>
          <span>(555) 014-2850</span>
        </li>
        <li class="contact-item">
          <svg class="contact-icon" viewBox="0 0 16 16"><circle cx="8" cy="8" r="8" fill="#fff"/><rect x="4" y="5" width="8" height="6" fill="#2d375f"/><path d="M4.5 9.5h7" stroke="#fff" stroke-width="0.8"/></svg>
          <span>(555) 014-2851</span>
        </li>
        <li class="contact-item">
          <svg class="contact-icon" viewBox="0 0 16 16"><circle cx="8" cy="8" r="8" fill="#fff"/><rect x="4" y="5" width="8" height="6" fill="#2d375f"/><path d="M4 5l4 3.2L12 5" stroke="#fff" stroke-width="0.8" fill="none"/></svg>
          <span>mtollandlaw@quillpost.example</span>
        </li>
        <li class="contact-item">
          <svg class="contact-icon" viewBox="0 0 16 16"><circle cx="8" cy="8" r="8" fill="#fff"/><circle cx="8" cy="8" r="4" fill="none" stroke="#2d375f" stroke-width="1"/><path d="M4 8h8M8 4c-2 2.5-2 5.5 0 8M8 4c2 2.5 2 5.5 0 8" fill="none" stroke="#2d375f" stroke-width="0.8"/></svg>
          <span>www.tollandlawfirm.example</span>
        </li>
      </ul>
    </div>
  </section>
</main>
</body>
</html>
```